Vantoria Podcast Cover Design

Looking for a podcast cover for a narrative (Re: fictional) podcast called Vantoria.

Here is a write up about the show:
Fascinated by nightmares, journalist Marla Penhove pursues the truth behind a popular vivid dreaming app. Sombrix allows users to experience their wildest dreams and beyond, but Marla discovers that for for some users, it's just the beginning of their worst nightmare.

Just to be clear, it's a fictional podcast about a podcast. :)

And just in case you don't know... here are the design requirements for podcast covers https://castmakers.brelvo.com/help/412-cover-guidelines

I'll attach some of the designs and images that my team likes... use it or not for inspiration

Target Market(s)

20-50, men and women, mostly United States

Industry/Entity Type

Podcast

Requirements
Nice to have
• Title of project

```html
<!DOCTYPE html>
<html lang="en">
<head>
<meta charset="utf-8">
<title>Vantoria Podcast Cover</title>
<link rel="stylesheet" href="https://fonts.googleapis.com/css2?family=Inter:wght@400;700;800&display=swap">
<style>
  :root {
    --page: #ffffff;
    --ink-light: #ffffff;
    --sky-deep: #1a2230;
    --sky-mid: #2c3646;
    --planet: #8a5a34;
    --cliff-gold: #b8921f;
    --cliff-dark: #1c1f22;
    --falls: #d9d2c8;
    --ground: #2a2526;
  }
  html, body {
    margin: 0;
    padding: 0;
    width: 1200px;
    height: 1200px;
    overflow: hidden;
    background: var(--page);
  }
  .canvas {
    position: relative;
    width: 1200px;
    height: 1200px;
    background: var(--page);
  }
  .cover {
    position: absolute;
    left: 126px;
    top: 126px;
    width: 948px;
    height: 948px;
    overflow: hidden;
  }
  .cover-art {
    position: absolute;
    inset: 0;
    background:
      radial-gradient(ellipse 22% 28% at 55% 18%, var(--planet) 0%, rgba(138,90,52,0.55) 55%, rgba(138,90,52,0) 100%),
      radial-gradient(ellipse 20% 55% at 52% 72%, var(--falls) 0%, rgba(217,210,200,0.5) 50%, rgba(217,210,200,0) 100%),
      radial-gradient(ellipse 35% 60% at 92% 55%, var(--cliff-gold) 0%, rgba(184,146,31,0.45) 55%, rgba(184,146,31,0) 100%),
      linear-gradient(180deg, var(--sky-deep) 0%, var(--sky-mid) 35%, var(--cliff-dark) 65%, var(--ground) 100%);
  }
  .title {
    position: absolute;
    left: 70px;
    top: 92px;
    margin: 0;
    font-family: "Inter", sans-serif;
    font-weight: 800;
    font-size: 214px;
    line-height: 1;
    letter-spacing: -0.055em;
    color: var(--ink-light);
  }
  .format {
    position: absolute;
    left: 70px;
    top: 304px;
    margin: 0;
    font-family: "Inter", sans-serif;
    font-weight: 400;
    font-size: 40px;
    line-height: 1;
    letter-spacing: -0.02em;
    color: var(--ink-light);
  }
  .host {
    position: absolute;
    left: 0;
    right: 0;
    top: 858px;
    margin: 0;
    text-align: center;
    font-family: "Inter", sans-serif;
    font-weight: 700;
    font-size: 56px;
    line-height: 1;
    letter-spacing: -0.03em;
    color: var(--ink-light);
  }
</style>
</head>
<body>
  <main class="canvas">
    <section class="cover">
      <div class="cover-art" role="img" aria-label="Surreal landscape: a large banded planet in a star-streaked night sky above golden mossy cliffs, a wide waterfall with a rainbow, and a hooded person standing with their back turned at its base"></div>
      <h1 class="title">Vantoria</h1>
      <p class="format">PODCAST</p>
      <p class="host">Marla Penhove</p>
    </section>
  </main>
</body>
</html>
```